Limousine Service Company Website

we need a website designed for a national limousine company with global capabilities (meaning they can service clients throughout the US and the world)

They service mostly corporate/business travelers, and groups and meetings, with a small portion of their business devoted to retail clients (special events and personal travel)

The overall look should be corporate, and we prefer a responsive design. We will need a home page, a fleet page (examples can be seen here: https://www.brovalecars.com/fleet
http://www.pennowayrides.com/our-fleet) and one interior page

Copy will be lorem epsum for now

We have no logo yet but can put a placeholder logo

```html
<!DOCTYPE html>
<html lang="en">
<head>
<meta charset="utf-8">
<title>Contact Us — Velmora Holdings</title>
<link rel="stylesheet" href="https://fonts.googleapis.com/css2?family=Arimo:wght@400;700&display=swap">
<style>
  :root {
    --ink: #333333;
    --ink-soft: #444444;
    --gold: #c9a24a;
    --gold-bright: #f2c21b;
    --gold-light: #e3c879;
    --night: #1c1c1c;
    --nav: #232323;
    --footer: #262626;
    --footer-text: #ffffff;
    --field-border: #d4d4d4;
    --field-focus: #9ab6cf;
    --paper: #ffffff;
  }
  * { box-sizing: border-box; margin: 0; padding: 0; }
  html, body { width: 1000px; height: 1200px; overflow: hidden; }
  body {
    position: relative;
    background: var(--paper);
    font-family: "Arimo", Helvetica, Arial, sans-serif;
    color: var(--ink);
  }
  .abs { position: absolute; }

  /* Top navigation */
  .site-nav {
    position: absolute; left: 0; top: 0; width: 1000px; height: 43px;
    background: linear-gradient(#2b2b2b, #1a1a1a);
    z-index: 5;
  }
  .site-nav a {
    position: absolute; top: 15px; font-size: 12px; color: #fff; text-decoration: none;
  }
  .site-nav a.is-active::after {
    content: ""; position: absolute; left: -4px; right: -4px; top: 24px; height: 2px;
    background: var(--gold-bright);
  }
  .nav-phone { position: absolute; left: 808px; top: 14px; font-size: 12px; color: #fff; display: flex; gap: 6px; align-items: center; }

  /* Hero */
  .hero-skyline {
    position: absolute; left: 0; top: 43px; width: 1000px; height: 230px;
    background: linear-gradient(180deg, #3a3a3a 0%, #1e1e1e 45%, #4a4a4a 100%);
  }
  .hero-wave { position: absolute; left: 0; top: 200px; width: 1000px; height: 110px; }
  .hero-title {
    position: absolute; left: 243px; top: 92px; font-size: 37px; font-weight: 700; color: #fff;
  }
  .hero-rule { position: absolute; left: 243px; top: 136px; width: 253px; height: 4px; background: var(--gold-bright); }
  .hero-sub { position: absolute; left: 245px; top: 152px; font-size: 15px; color: #fff; }
  .hero-vehicle {
    position: absolute; left: 600px; top: 167px; width: 264px; height: 120px; border-radius: 40px 50px 14px 14px;
    background: radial-gradient(ellipse at 50% 45%, #3a3a3a 0%, #111 70%, rgba(17,17,17,0.0) 100%);
  }

  /* Address */
  .section-title { position: absolute; font-size: 16px; color: var(--gold); font-weight: 400; }
  .address-block {
    position: absolute; left: 51px; top: 347px; height: 136px; border-left: 3px solid var(--gold);
    padding-left: 13px; font-size: 11px; line-height: 19.6px; color: var(--ink);
  }
  .address-block .company { font-weight: 700; color: #111; }

  /* Contact form */
  .form-intro { position: absolute; left: 360px; top: 341px; width: 420px; font-size: 11px; line-height: 14.5px; color: var(--ink); }
  .field-label { position: absolute; left: 360px; font-size: 11px; color: var(--ink); }
  .field {
    position: absolute; left: 360px; width: 409px; border: 1px solid var(--field-border);
    background: linear-gradient(#ffffff, #f6f6f6);
  }
  .field.is-focused { border-color: var(--field-focus); box-shadow: 0 0 3px rgba(120,160,200,0.5); background: #fff; }
  .form-divider { position: absolute; left: 356px; top: 727px; width: 414px; height: 1px; background: #eeeeee; }
  .send-button {
    position: absolute; left: 665px; top: 737px; width: 104px; height: 30px; border-radius: 2px;
    background: linear-gradient(#e8cd82, #c9a24a); color: #fff; font-weight: 700; font-size: 14px;
    display: flex; align-items: center; justify-content: center;
  }

  /* Footer */
  .site-footer {
    position: absolute; left: 0; top: 825px; width: 1000px; height: 375px;
    background: var(--footer); border-top: 3px solid var(--gold);
  }
  .footer-col { position: absolute; font-size: 11px; color: var(--footer-text); line-height: 21.3px; }
  .footer-col h4 { font-size: 13px; font-weight: 400; color: var(--gold); line-height: 21.3px; margin-bottom: 0; }
  .footer-col .spaced { margin-top: 7px; }
  .footer-logo { position: absolute; left: 731px; top: 57px; width: 160px; text-align: center; font-size: 11px; color: #fff; }
  .footer-contact { position: absolute; right: 111px; top: 99px; text-align: right; font-size: 11px; line-height: 21.3px; color: #fff; }
  .social { position: absolute; top: 227px; width: 20px; height: 20px; background: var(--gold); border-radius: 2px; }
  .accreditation { position: absolute; left: 83px; top: 238px; width: 74px; height: 29px; border-radius: 4px; background: #1f5a7a; border: 1px solid #8aa9bc; }
  .footer-legal { position: absolute; left: 83px; top: 294px; width: 545px; font-size: 7.4px; line-height: 11px; color: #fff; }
  .copyright { position: absolute; left: 83px; top: 345px; font-size: 8px; color: #fff; }
</style>
</head>
<body>

<nav class="site-nav">
  <a href="#" style="left:411px">Home</a>
  <a href="#" style="left:472px">About Us</a>
  <a href="#" style="left:551px">Limos</a>
  <a href="#" style="left:612px">Our Services</a>
  <a href="#" class="is-active" style="left:708px">Contact Us</a>
  <span class="nav-phone">
    <svg width="11" height="11" viewBox="0 0 24 24" aria-hidden="true"><path fill="#fff" d="M6.6 10.8a15.1 15.1 0 0 0 6.6 6.6l2.2-2.2a1 1 0 0 1 1-.25 11.4 11.4 0 0 0 3.6.57 1 1 0 0 1 1 1V20a1 1 0 0 1-1 1A17 17 0 0 1 3 4a1 1 0 0 1 1-1h3.5a1 1 0 0 1 1 1c0 1.25.2 2.45.57 3.57a1 1 0 0 1-.25 1z"/></svg>
    Call Us: 01800. 482.907
  </span>
</nav>

<div class="hero-skyline" role="img" aria-label="Night-time city skyline photograph in dark grey tones"></div>
<svg class="hero-wave" viewBox="0 0 1000 110" preserveAspectRatio="none" aria-hidden="true">
  <path d="M0 22 C220 28 420 30 600 46 C720 56 860 42 1000 20 L1000 110 L0 110 Z" fill="#e0a900"/>
  <path d="M0 38 C220 36 420 42 600 56 C720 66 860 62 1000 52 L1000 110 L0 110 Z" fill="#f5c518"/>
  <path d="M0 42 C240 40 440 50 600 64 C730 76 870 80 1000 70 L1000 110 L0 110 Z" fill="#ffffff"/>
</svg>
<div class="hero-vehicle" role="img" aria-label="Black luxury SUV photograph"></div>
<h1 class="hero-title">Contact Us</h1>
<div class="hero-rule"></div>
<p class="hero-sub">Have a Question? Drop us a message</p>

<h2 class="section-title" style="left:49px; top:314px">Our Address</h2>
<address class="address-block" style="font-style:normal">
  <div class="company">Velmora Holdings LLC</div>
  <div>218 Harlow Avenue Riverton,</div>
  <div>NY 10452</div>
  <div>Corporate Headquarters:</div>
  <div>1-800-555-0142</div>
  <div>Customer Service: 1-800-555-0187</div>
  <div>Email us at: info@VelmoraHoldings.com</div>
</address>

<h2 class="section-title" style="left:360px; top:314px">Get In Touch</h2>
<p class="form-intro">We’d love to hear from you. Give us a few details so we can put you in touch with the right person.</p>

<label class="field-label" style="top:389px">Your Name:</label>
<div class="field is-focused" style="top:412px; height:29px"></div>
<label class="field-label" style="top:459px">Your Email:</label>
<div class="field" style="top:483px; height:28px"></div>
<label class="field-label" style="top:530px">Your Phone Number:</label>
<div class="field" style="top:553px; height:28px"></div>
<label class="field-label" style="top:602px">Your Message:</label>
<div class="field" style="top:627px; height:72px"></div>
<div class="form-divider"></div>
<div class="send-button">Send</div>

<footer class="site-footer">
  <div class="footer-col" style="left:85px; top:27px">
    <h4>Get to Know Us</h4>
    <div>Lorem ipsum dolor</div><div>The Limo Difference</div><div>Car Service Fleet</div>
    <div>Our Limo Service Rates</div><div>Our Car Service App</div><div>Management Team</div>
    <div>Press</div><div>Blog</div>
  </div>
  <div class="footer-col" style="left:248px; top:27px">
    <h4>Products and Services</h4>
    <div>Lorem ipsum dolor</div><div>The Limo Difference</div><div>Car Service Fleet</div>
    <div>Our Limo Service Rates</div><div>Our Car Service App</div><div>Management Team</div>
    <div>Press</div><div>Blog</div>
  </div>
  <div class="footer-col" style="left:439px; top:27px">
    <h4>Get to Know Us</h4>
    <div>Lorem ipsum dolor</div><div>The Limo Difference</div><div>Car Service Fleet</div>
    <h4 class="spaced">Get to Know Us</h4>
    <div>Lorem ipsum dolor</div><div>The Limo Difference</div><div>Car Service Fleet</div>
  </div>

  <div class="footer-logo">YOUR LOGO</div>
  <div class="footer-contact">
    <div>Corporate Headquarters: 1-800-555-0142</div>
    <div>Customer Service: 1-800-555-0187</div>
    <div>Velmora Holdings LLC</div>
    <div>218 Harlow Avenue</div>
    <div>Riverton, NY 10452</div>
  </div>

  <span class="social" style="left:805px"></span>
  <span class="social" style="left:837px"></span>
  <span class="social" style="left:869px"></span>

  <div class="accreditation"></div>

  <p class="footer-legal">Lorem ipsum dolor sit amet, consectetur adipisicing elit, sed do eiusmod tempor incididunt ut labore et dolore magna aliqua. Ut enim ad minim veniam, quis nostrud exercitation ullamco laboris nisi ut aliquip ex ea commodo consequat. Duis aute irure dolor in reprehenderit in voluptate velit esse cillum dolore eu fugiat nulla pariatur. Excepteur sint occaecat cupidatat non proident, sunt in culpa qui officia deserunt mollit anim id</p>
  <p class="copyright">© Copyright 2014 Velmora Holdings LLC</p>
</footer>

</body>
</html>
```